We need to design Labels of one of Our Brand BrivaLune Lotion.

The purpose of this product is to keep mosquitoes away.
There are 3 variants of this lotion. So we need 3 designs for the product. These variants details are mentioned below:

1) Mosquito Repellent Lotion with Lavender Fragrance.
2) Mosquito Repellent Lotion with Natural Ingredients.
3) Mosquito Repellent Lotion for kids.

Kindly note the bottle will be WHITE for all the variants. Cap will of the bottle will be with accordance to the color of label. In the picture it is red just for presentation.

Kindly share design of Repellent Lotion with Lavendar Fragrance initially and if we give your positive feedback, then you may add further variants of the design.

The bottle shape is attached along with keylines. Also attaching logo. If there is any other option for logo, you can suggest which we would probably keep our existing logo.

Target Market(s)

B+, B, C+

Industry/Entity Type

Product

Colors
a54499
6b449b

Requirements
Must have
• Mosquito
• 100ml
Nice to have
• Purple color as background
Should not have
• Lavendar flower

```html
<!DOCTYPE html>
<html lang="en">
<head>
<meta charset="utf-8">
<title>BrivaLune Mosquito Repellent Label</title>
<link rel="stylesheet" href="https://fonts.googleapis.com/css2?family=Oswald:wght@400;500;700&display=swap">
<style>
  :root {
    --canvas: #ffffff;
    --ink: #1a1a1a;
    --label-yellow: #f7e526;
    --label-yellow-deep: #fdd20f;
    --label-purple: #6a1f5c;
    --label-navy: #1f2460;
    --blue-deep: #2b3796;
    --blue-light: #3a9bd9;
    --badge-blue: #1f6fc0;
    --warning-yellow: #ffd800;
    --insect-area: #5a3a3a;
    --white: #ffffff;
  }
  html, body {
    margin: 0;
    padding: 0;
    width: 1200px;
    height: 1000px;
    overflow: hidden;
    background: var(--canvas);
  }
  .artboard {
    position: relative;
    width: 1200px;
    height: 1000px;
  }
  .artboard svg { position: absolute; left: 0; top: 0; }
  .dimension-text {
    font-family: "Oswald", "Arial Narrow", sans-serif;
    font-weight: 400;
    font-size: 20px;
    fill: var(--ink);
  }
  .tagline-small {
    font-family: "Oswald", "Arial Narrow", sans-serif;
    font-weight: 400;
    font-size: 15px;
    fill: var(--ink);
  }
  .badge-text {
    font-family: "Oswald", "Arial Narrow", sans-serif;
    font-weight: 700;
    font-size: 30px;
    fill: var(--white);
  }
  .brand-name {
    font-family: "Oswald", "Arial Narrow", sans-serif;
    font-weight: 700;
    font-size: 78px;
    fill: var(--white);
  }
  .product-type {
    font-family: "Oswald", "Arial Narrow", sans-serif;
    font-weight: 700;
    font-size: 30px;
    fill: var(--white);
  }
  .fragrance {
    font-family: "Oswald", "Arial Narrow", sans-serif;
    font-weight: 400;
    font-size: 15px;
    fill: var(--white);
  }
  .claim {
    font-family: "Oswald", "Arial Narrow", sans-serif;
    font-weight: 500;
    font-size: 26px;
    fill: var(--white);
  }
</style>
</head>
<body>
<main class="artboard">
  <svg width="1200" height="1000" viewBox="0 0 1200 1000">
    <defs>
      <clipPath id="label-outline">
        <path d="M170,205 Q165,180 200,172 Q355,145 520,185 Q545,195 540,220 Q528,260 535,300 Q552,520 535,720 Q520,800 528,870 Q532,907 498,908 L238,908 Q200,906 200,870 Q205,800 182,720 Q158,520 175,300 Q180,260 170,205 Z"/>
      </clipPath>
      <linearGradient id="yellow-band" x1="0" y1="0" x2="1" y2="0">
        <stop offset="0" stop-color="var(--label-yellow-deep)"/>
        <stop offset="1" stop-color="var(--label-yellow)"/>
      </linearGradient>
      <linearGradient id="blue-band" x1="0" y1="1" x2="1" y2="0">
        <stop offset="0" stop-color="var(--blue-deep)"/>
        <stop offset="0.5" stop-color="#2f5fb5"/>
        <stop offset="1" stop-color="var(--blue-light)"/>
      </linearGradient>
      <linearGradient id="badge-fill" x1="0" y1="0" x2="0" y2="1">
        <stop offset="0" stop-color="#4fb2ec"/>
        <stop offset="1" stop-color="var(--badge-blue)"/>
      </linearGradient>
    </defs>

    <!-- dimension marks -->
    <g class="dimensions" stroke="var(--ink)" stroke-width="1.2" fill="none">
      <line x1="166" y1="142" x2="546" y2="142"/>
      <polyline points="174,137 164,142 174,147"/>
      <polyline points="538,137 548,142 538,147"/>
      <line x1="145" y1="172" x2="145" y2="912"/>
      <polyline points="140,180 145,170 150,180"/>
      <polyline points="140,904 145,914 150,904"/>
    </g>
    <text class="dimension-text" x="347" y="134" text-anchor="middle">44 mm</text>
    <text class="dimension-text" x="0" y="0" text-anchor="middle" transform="translate(133,545) rotate(-90)">85 mm</text>

    <!-- label -->
    <g class="label" clip-path="url(#label-outline)">
      <rect class="label-base" x="150" y="140" width="420" height="790" fill="var(--label-purple)"/>
      <path class="top-band" d="M150,140 H570 V278 Q380,290 150,328 Z" fill="url(#yellow-band)"/>
      <path class="top-band-edge" d="M150,328 Q380,290 570,278" stroke="var(--label-navy)" stroke-width="5" fill="none"/>
      <path class="bottom-band" d="M150,785 Q330,720 570,728 V930 H150 Z" fill="url(#blue-band)"/>
      <path class="bottom-band-edge" d="M150,785 Q330,720 570,728" stroke="var(--label-navy)" stroke-width="5" fill="none"/>
    </g>

    <text class="tagline-small" x="494" y="269" text-anchor="end">HARMLESS TO THE SKIN</text>

    <g class="new-badge">
      <ellipse cx="256" cy="305" rx="52" ry="35" fill="url(#badge-fill)" stroke="var(--white)" stroke-width="3"/>
      <text class="badge-text" x="256" y="316" text-anchor="middle">NEW</text>
    </g>

    <text class="brand-name" x="355" y="472" text-anchor="middle">BrivaLune</text>

    <text class="product-type" x="360" y="581" text-anchor="middle">MOSQUITO REPELLENT</text>

    <g class="no-mosquito-sign">
      <circle cx="297" cy="715" r="70" fill="var(--insect-area)" opacity="0.35" role="img" aria-label="Photograph of a mosquito"/>
      <circle cx="297" cy="715" r="78" fill="none" stroke="var(--warning-yellow)" stroke-width="14"/>
      <line x1="243" y1="660" x2="352" y2="770" stroke="var(--warning-yellow)" stroke-width="14"/>
    </g>

    <text class="fragrance" x="510" y="712" text-anchor="end">LAVENDER FRAGRANCE</text>

    <text class="claim" x="355" y="837" text-anchor="middle">PREVENTION AGAINST</text>
    <text class="claim" x="355" y="868" text-anchor="middle">DENGUE AND MALARIA</text>
  </svg>
</main>
</body>
</html>
```